Patient Transport company website design

We're a small patient transport company desiring a big company image. Our company is called Pelnorva. We're based in Houston, TX. Our mission is to provide a safe, cost effective, and convenient mode of local transportation. Similar to a taxi service but more patient friendly.
We would like to see designs that illustrate our mission and have a big company online presence. We like bright colors but not too bright and cartoon-like. Our target audience are patients but we also cater to elderly as well as those who might not have reliable transportation.
We're not an emergency transport service. We're not a taxi service. We're more like a shuttle service... a compromise between the two. Photography for the site should show patients and elderly riding in normal (unmarked vehicles) to and from dr visits, etc.
Our competitors' websites are listed here to give you a general idea about the industry.
http://www.trelvanridecare.example/
http://www.brivashuttle.example/
http://www.quomelwayshuttles.example/
Target Market(s)
Patients needing transportation assistance and Elderly as well.
Industry/Entity Type
Taxi
Requirements
Must have
- Website must be done in wordpress. Website must have the following links:
Services, About, Book a trip, jobs, control panel, clients
Should use photos communicating safe travels to and from... particularly with Elderly if possible.
Design should be consistent with attached logo.
Nice to have
- Bright colors

```html
<!DOCTYPE html>
<html lang="en">
<head>
<meta charset="utf-8">
<title>Pelnorva – Patient Transportation Services</title>
<link rel="stylesheet" href="https://fonts.googleapis.com/css2?family=Open+Sans:wght@400;600&display=swap">
<style>
:root{
  --white:#ffffff;
  --brand-blue:#1d4f91;
  --brand-green:#9bc53d;
  --nav-cyan:#08a6c8;
  --sky:#a6dcee;
  --card-navy:#0f4a8a;
  --charcoal:#1f2227;
  --tab-teal:#1b7b8c;
  --tab-teal-dark:#135f6d;
  --field:#33373e;
  --footer-blue:#0d4d8b;
  --text-grey:#8a8a8a;
  --link-blue:#2a5d9c;
  --social-blue:#3b5ba4;
  --social-cyan:#28aee3;
}
*{margin:0;padding:0;box-sizing:border-box}
html,body{width:1200px;height:1136px;overflow:hidden;background:var(--white)}
body{position:relative;font-family:"Open Sans",Arial,sans-serif}
.abs{position:absolute}

/* header */
.brand{left:172px;top:14px;width:180px;height:100px}
.brand-mark{left:52px;top:6px;width:34px;height:34px;border-radius:50%;background:var(--brand-blue)}
.brand-name{left:10px;top:44px;font-size:34px;font-weight:400;color:var(--brand-blue);line-height:1}
.brand-tag{left:2px;top:87px;font-size:10px;font-weight:600;color:var(--brand-green);white-space:nowrap}
.search{left:609px;top:31px;width:309px;height:31px;display:flex}
.search-field{flex:1;border:1px solid #c9d9a3;background:#f3f3f3;font-size:11px;color:#888;padding:8px 10px}
.search-btn{width:97px;background:var(--brand-green);color:var(--white);font-size:13px;font-weight:600;display:flex;align-items:center;justify-content:center}
.social{width:32px;height:32px;border-radius:50%}
.social.blue{background:var(--social-blue)}
.social.cyan{background:var(--social-cyan)}
.top-links{right:175px;top:90px;font-size:13px;color:var(--link-blue);letter-spacing:.5px;white-space:nowrap}
.top-links .sep{color:#aaa;margin:0 8px}
.top-links .alt{color:var(--brand-green)}
.top-links .staff{color:var(--nav-cyan)}

/* nav */
.main-nav{left:0;top:124px;width:1200px;height:37px;background:var(--nav-cyan);display:flex;justify-content:center;align-items:center}
.main-nav span{color:var(--white);font-size:17px;padding:0 24px;border-left:1px solid rgba(255,255,255,.35);line-height:22px;white-space:nowrap}
.main-nav span:first-child{border-left:none}

/* hero */
.hero{left:166px;top:161px;width:866px;height:357px;background:linear-gradient(120deg,#9a9890 0%,#c9524a 35%,#e9e6e0 55%,#b5342f 75%,#7d7a74 100%)}
.hero-caption{left:166px;top:465px;width:866px;height:53px;background:rgba(20,20,20,.78);display:flex;align-items:center;justify-content:center;color:var(--brand-green);font-size:27px;letter-spacing:1px;white-space:nowrap}
.hero-arrow{top:465px;width:35px;height:53px;background:#6e8a2c;color:var(--white);display:flex;align-items:center;justify-content:center}

/* features */
.features{left:0;top:518px;width:1200px;height:372px;background:var(--sky)}
.card{top:541px;width:247px;height:316px;background:var(--white);box-shadow:0 3px 5px rgba(0,0,0,.35)}
.card-head{left:0;top:0;width:100%;height:101px;background:var(--card-navy)}
.card-title{left:0;top:14px;width:100%;text-align:center;color:var(--white);font-size:17px;white-space:nowrap}
.card-photo{left:21px;top:47px;width:206px;height:127px;border-bottom:2px solid var(--card-navy)}
.card-social{top:182px;width:32px;height:32px;border-radius:50%}
.card-text{left:21px;top:230px;width:206px;font-size:10.5px;line-height:14px;color:var(--text-grey);text-align:justify}

/* lower */
.lower{left:0;top:890px;width:1200px;height:187px;background:var(--charcoal)}
.tab{top:868px;width:250px;height:53px}
.tab-label{left:24px;top:28px;color:var(--white);font-size:16px;white-space:nowrap}
.list{top:936px;width:200px;list-style:none}
.list li{position:relative;padding-left:24px;color:var(--white);font-size:11px;line-height:14px;margin-bottom:13px}
.list li::before{content:"";position:absolute;left:0;top:6px;width:8px;height:8px;border-radius:50%;background:var(--brand-green)}
.field{left:780px;width:213px;height:30px;background:var(--field);color:#888;font-size:11px;padding:8px 10px}
.submit{left:918px;top:1024px;width:75px;height:29px;background:var(--brand-green);color:var(--charcoal);font-size:12px;display:flex;align-items:center;justify-content:center}

/* footer */
.footer-links{left:0;top:1077px;width:1200px;height:31px;background:var(--footer-blue);color:var(--white);font-size:11px;display:flex;align-items:center;justify-content:center;white-space:pre}
.copyright{left:0;top:1108px;width:1200px;height:28px;background:var(--brand-green);color:var(--charcoal);font-size:11px;display:flex;align-items:center;justify-content:center}
</style>
</head>
<body>

<header>
  <div class="abs brand">
    <div class="abs brand-mark"></div>
    <div class="abs brand-name">Pelnorva</div>
    <div class="abs brand-tag">Patient Transportation Services</div>
  </div>
  <div class="abs search"><div class="search-field">Type Here . . .</div><div class="search-btn">SEARCH</div></div>
  <div class="abs social blue" style="left:950px;top:31px" role="img" aria-label="Social profile"></div>
  <div class="abs social cyan" style="left:993px;top:31px" role="img" aria-label="Social profile"></div>
  <div class="abs top-links">HOME<span class="sep">|</span><span class="alt">CONTACT US</span><span class="sep">|</span><span class="staff">STAFF&nbsp; LOGIN</span></div>
</header>

<nav class="abs main-nav">
  <span>About Us</span><span>Services</span><span>Book a Trip</span><span>Jobs</span><span>Clients</span><span>Control Panel</span>
</nav>

<section>
  <div class="abs hero" role="img" aria-label="Care staff helping a patient into a transport vehicle"></div>
  <div class="abs hero-caption">PATIENT&nbsp; TRANSPORTATION&nbsp;&nbsp; SERVICES</div>
  <div class="abs hero-arrow" style="left:166px">
    <svg width="10" height="14" viewBox="0 0 10 14"><path d="M8 1 2 7l6 6" fill="none" stroke="#fff" stroke-width="2.5"/></svg>
  </div>
  <div class="abs hero-arrow" style="left:997px">
    <svg width="10" height="14" viewBox="0 0 10 14"><path d="M2 1l6 6-6 6" fill="none" stroke="#fff" stroke-width="2.5"/></svg>
  </div>
</section>

<section class="abs features"></section>

<article class="abs card" style="left:193px">
  <div class="abs card-head"></div>
  <div class="abs card-title">WE ARE PROFESSIONAL</div>
  <div class="abs card-photo" role="img" aria-label="Care staff assisting a patient in a hospital bed" style="background:linear-gradient(135deg,#cfd6dc,#6f8fb5 50%,#c24a55)"></div>
  <div class="abs card-social" style="left:86px;background:var(--social-blue)"></div>
  <div class="abs card-social" style="left:130px;background:var(--social-cyan)"></div>
  <p class="abs card-text">Lorem Ipsum Dolor sit ame, cons adipisi elit dower hen.&nbsp;&nbsp; Lorem Ipsum Dolor sit ame, cons adipisi elit dower hen.</p>
</article>

<article class="abs card" style="left:480px">
  <div class="abs card-head"></div>
  <div class="abs card-title">PATIENT CARING</div>
  <div class="abs card-photo" role="img" aria-label="Doctor speaking with an elderly patient" style="background:linear-gradient(135deg,#e6ddd6,#c7b7ad 45%,#eef0f2)"></div>
  <div class="abs card-social" style="left:86px;background:var(--social-blue)"></div>
  <div class="abs card-social" style="left:130px;background:var(--social-cyan)"></div>
  <p class="abs card-text">Lorem Ipsum Dolor sit ame, cons adipisi elit dower hen.&nbsp;&nbsp; Lorem Ipsum Dolor sit ame, cons adipisi elit dower hen.</p>
</article>

<article class="abs card" style="left:760px">
  <div class="abs card-head"></div>
  <div class="abs card-title">TECHNOLOGICALLY AHEAD</div>
  <div class="abs card-photo" role="img" aria-label="Stethoscope resting on a tablet" style="background:linear-gradient(135deg,#f2f3f4,#b9c4cb 55%,#6fb7c9)"></div>
  <div class="abs card-social" style="left:86px;background:var(--social-blue)"></div>
  <div class="abs card-social" style="left:130px;background:var(--social-cyan)"></div>
  <p class="abs card-text">Lorem Ipsum Dolor sit ame, cons adipisi elit dower hen.&nbsp;&nbsp; Lorem Ipsum Dolor sit ame, cons adipisi elit dower hen.</p>
</article>

<section class="abs lower"></section>

<div class="abs tab" style="left:191px">
  <svg class="abs" width="250" height="53" viewBox="0 0 250 53" style="left:0;top:0">
    <polygon points="0,22 210,22 220,53 0,53" fill="var(--tab-teal)"/>
    <polygon points="205,22 235,22 250,53 220,53" fill="var(--tab-teal-dark)"/>
    <polygon points="228,0 236,0 250,53 242,53" fill="var(--tab-teal)"/>
  </svg>
  <div class="abs tab-label">CASE HISTORIES</div>
</div>
<div class="abs tab" style="left:479px">
  <svg class="abs" width="250" height="53" viewBox="0 0 250 53" style="left:0;top:0">
    <polygon points="0,22 210,22 220,53 0,53" fill="var(--tab-teal)"/>
    <polygon points="205,22 235,22 250,53 220,53" fill="var(--tab-teal-dark)"/>
    <polygon points="228,0 236,0 250,53 242,53" fill="var(--tab-teal)"/>
  </svg>
  <div class="abs tab-label">LATEST NEWS</div>
</div>
<div class="abs tab" style="left:760px">
  <svg class="abs" width="250" height="53" viewBox="0 0 250 53" style="left:0;top:0">
    <polygon points="0,22 210,22 220,53 0,53" fill="var(--tab-teal)"/>
    <polygon points="205,22 235,22 250,53 220,53" fill="var(--tab-teal-dark)"/>
    <polygon points="228,0 236,0 250,53 242,53" fill="var(--tab-teal)"/>
  </svg>
  <div class="abs tab-label">SUBSCRIBE NEWSLETTER</div>
</div>

<ul class="abs list" style="left:213px">
  <li>Lorem Ipsum Dolor sit ame, cons adipisi elit dower hen.</li>
  <li>Lorem Ipsum Dolor sit ame, cons adipisi elit dower hen.</li>
  <li>Lorem Ipsum Dolor sit ame, cons adipisi elit dower hen.</li>
</ul>
<ul class="abs list" style="left:500px">
  <li>Lorem Ipsum Dolor sit ame, cons adipisi elit dower hen.</li>
  <li>Lorem Ipsum Dolor sit ame, cons adipisi elit dower hen.</li>
  <li>Lorem Ipsum Dolor sit ame, cons adipisi elit dower hen.</li>
</ul>

<div class="abs field" style="top:943px">Name</div>
<div class="abs field" style="top:983px">Email Id</div>
<div class="abs submit">SUBMIT</div>

<footer>
  <div class="abs footer-links">Home | About Us | Services | Book a Trip | Jobs | Clients | Control Panel  |  Contact Us  |  Sitemap  |  Privacy &amp; Accessibility</div>
  <div class="abs copyright">© 2013&nbsp; Pelnorva&nbsp; (Patient Transportation Services)</div>
</footer>

</body>
</html>
```